Dynamic Templates

Our company hosts web stores for our clients. They can set up as many as they wish on our platform, and select from the stock templates we provide. We are looking to increase the number of available stock templates.

Because our users can dynamically control many of the template elements - specifically colors - they have to be flexible and abide by certain rules. These rules are spelled out in the attached documents.

Here are links to two of our most used templates:
http://brivelta.tondashop.example/
http://quillorn.tondashop.example/

Templates need to have a landing page (what you see when first clicking one of the above links). There also needs to be a category page (what you see when clicking any category) and a product detail page (what you see when you arrive at an individual product, where there are various cart options like Buy Now or Request Info).

```html
<!DOCTYPE html>
<html lang="en">
<head>
<meta charset="utf-8">
<title>Tondashop – Promotional Products</title>
<link rel="stylesheet" href="https://fonts.googleapis.com/css2?family=Gelasio&family=Noto+Serif&family=Source+Sans+3:wght@400;600&display=swap">
<style>
:root{
  --header-bg:#3a4248;
  --header-top:#8e9ea3;
  --band-bg:#93a2a6;
  --band-dark:#7d8c91;
  --panel:#2b3236;
  --panel-border:#4f585e;
  --ink:#222;
  --heading:#333;
  --footer-bg:#3a4147;
  --footer-text:#d4d8da;
  --footer-line:#23292d;
  --accent:#f39a12;
  --accent-light:#ffc23a;
  --white:#fff;
}
*{margin:0;padding:0;box-sizing:border-box}
html,body{width:1150px;height:1200px;overflow:hidden}
body{position:relative;background:var(--white);font-family:"Noto Serif",Georgia,serif;color:var(--ink)}
.site-header{position:absolute;left:0;top:0;width:1150px;height:129px;background:linear-gradient(var(--header-top) 0 9px,#4a5358 9px 11px,var(--header-bg) 11px);}
.brand{position:absolute;left:100px;top:35px;width:260px;height:70px;background:var(--panel);border:1px solid var(--panel-border);border-radius:6px;display:flex;align-items:center;padding-left:18px;gap:10px}
.brand-dot{width:34px;height:34px;border-radius:50%;background:var(--accent)}
.brand-name{font-family:"Source Sans 3",Arial,sans-serif;font-size:22px;color:var(--white);font-weight:400}
.contact-box{position:absolute;left:820px;top:35px;width:230px;height:50px;background:var(--panel);border:1px solid var(--panel-border);border-radius:6px;text-align:right;padding:10px 14px 0 0;font-family:"Source Sans 3",Arial,sans-serif;font-size:12px;letter-spacing:1px;color:var(--white);line-height:15px}
.product-band{position:absolute;left:0;top:129px;width:1150px;height:272px;background:linear-gradient(var(--band-dark),var(--band-bg) 15%,var(--band-bg) 85%,#a6b3b6);border-bottom:1px solid #c9d0d2}
.product-card{position:absolute;top:16px;width:230px;height:240px;background:var(--white);border-radius:7px;box-shadow:0 1px 3px rgba(0,0,0,.35);padding:14px}
.product-card div{width:100%;height:100%;border-radius:4px}
.content{position:absolute;left:0;top:401px;width:1150px;height:413px;background:linear-gradient(#e9eaea,#fff 40px,#fff 380px,#ececec);border-bottom:2px solid #d5d8da}
h1{position:absolute;left:100px;top:40px;font-family:"Gelasio",Georgia,serif;font-weight:400;font-size:37px;line-height:37px;color:var(--heading)}
h2{position:absolute;left:98px;top:228px;font-family:"Gelasio",Georgia,serif;font-weight:400;font-size:30px;color:var(--heading)}
.intro{position:absolute;left:100px;top:122px;width:640px;font-size:13px;line-height:20px}
.resource{position:absolute;left:100px;top:280px;width:680px;font-size:13px;line-height:20px}
.cta{position:absolute;left:820px;top:44px;width:230px;height:46px;border-radius:6px;background:repeating-linear-gradient(-45deg,var(--accent) 0 6px,#f7a91f 6px 12px);border:1px solid #e08a00;box-shadow:inset 0 1px 0 var(--accent-light);font-family:"Gelasio",Georgia,serif;font-style:italic;font-size:25px;color:var(--white);padding:6px 0 0 16px;text-decoration:none}
.site-footer{position:absolute;left:0;top:815px;width:1150px;height:385px;background:var(--footer-bg);color:var(--footer-text)}
.tab{position:absolute;top:30px;height:36px;background:var(--panel);border:1px solid var(--panel-border);border-radius:6px;font-family:"Gelasio",Georgia,serif;font-size:17px;color:var(--footer-text);padding:7px 0 0 11px}
.divider{position:absolute;top:28px;width:1px;height:248px;background:var(--footer-line);box-shadow:1px 0 0 #4a5258}
.link-list{position:absolute;top:82px;list-style:none;font-size:12px;line-height:18px}
.link-list li::before{content:"→";color:#8b959a;font-size:10px;margin-right:4px}
.search{position:absolute;left:820px;top:85px;width:164px;height:25px;border-radius:12px;background:var(--white);border:1px solid #aaa}
.search svg{position:absolute;right:10px;top:6px}
.go{position:absolute;left:994px;top:85px;width:42px;height:25px;border-radius:12px;background:linear-gradient(#fff,#ccc);color:#333;font-family:"Gelasio",Georgia,serif;font-style:italic;font-weight:700;font-size:14px;text-align:center;line-height:25px}
.footer-contact{position:absolute;left:820px;top:190px;font-size:12px;line-height:18px}
.copyright{position:absolute;left:100px;top:323px;font-size:12px}
</style>
</head>
<body>
<header class="site-header">
  <div class="brand"><span class="brand-dot"></span><span class="brand-name">Tondashop</span></div>
  <div class="contact-box">(555) 014-2278<br>info@tondashop.example</div>
</header>

<section class="product-band">
  <div class="product-card" style="left:100px"><div role="img" aria-label="Red gel mouse pad" style="background:radial-gradient(ellipse at center,#c8353f 55%,#fff 57%)"></div></div>
  <div class="product-card" style="left:340px"><div role="img" aria-label="Black travel mug with blue grip sleeve" style="background:linear-gradient(#fff 8%,#1d1e22 8%,#1d1e22 52%,#2d4a9c 52%,#2d4a9c 92%,#fff 92%) center/46% 100% no-repeat"></div></div>
  <div class="product-card" style="left:580px"><div role="img" aria-label="Clear travel kit with four bottles" style="background:linear-gradient(#fff 20%,#eef1f2 20%,#dde3e5 80%,#fff 80%)"></div></div>
  <div class="product-card" style="left:820px"><div role="img" aria-label="Brown toy bank figure" style="background:radial-gradient(ellipse at center,#6e4a3a 42%,#fff 44%)"></div></div>
</section>

<main class="content">
  <h1>Welcome To The Future<br>of Promotional Products!</h1>
  <p class="intro">Gone are the days of searching through dog-eared catalogs or trying to make sense of complicated product websites. We do the work for you! We've taken only the very best and most current products and placed them in easy-to-use categories designed for your needs. Take a look at our selection - quality products at excellent prices.</p>
  <h2>Enjoy This Amazing New Resource</h2>
  <p class="resource">We know you don't have time to waste; so we've cut to the chase and made it simple! But keep in mind, we do have access to over a million products - so if you don't see what you're looking for or have a special theme or request, let us know - we'll find it!</p>
  <a class="cta" href="#">Start Shopping »</a>
</main>

<footer class="site-footer">
  <div class="tab" style="left:100px;width:166px">Shop By Category</div>
  <ul class="link-list" style="left:100px">
    <li>Apparel</li><li>Auto</li><li>Awards &amp; Recognition</li><li>Bags &amp; Totes</li><li>Business Supplies</li><li>Calendars, Books &amp; Cards</li><li>Caps &amp; Hats</li><li>Clocks &amp; Watches</li><li>Company Outings</li><li>Computer</li><li>Corporate Gifts</li>
  </ul>
  <ul class="link-list" style="left:271px">
    <li>Desktop &amp; Office</li><li>Eco Friendly</li><li>Electronics</li><li>Executive Gifts</li><li>Food, Candy &amp; Drink</li><li>Games &amp; Novelties</li><li>Gift Sets</li><li>Golf, Sports &amp; Outdoors</li><li>Healthcare &amp; Safety</li><li>Holiday</li><li>Home &amp; Housewares</li>
  </ul>
  <ul class="link-list" style="left:426px">
    <li>Keychains</li><li>Mugs &amp; Drinkware</li><li>Notebooks &amp; Folios</li><li>Pocket &amp; Purse</li><li>Stress Balls &amp; Relievers</li><li>Tools &amp; Hardware</li><li>Tradeshows &amp; Events</li><li>Travel &amp; Luggage</li><li>Writing Instrument</li>
  </ul>
  <span class="divider" style="left:581px"></span>
  <div class="tab" style="left:599px;width:166px">Shop By Price</div>
  <ul class="link-list" style="left:603px">
    <li>Under $5</li><li>$5 - $10</li><li>$10 - $20</li><li>$20 - $50</li><li>$50 - $100</li><li>$100 - $200</li><li>Over $200</li>
  </ul>
  <span class="divider" style="left:795px"></span>
  <div class="tab" style="left:820px;width:166px">Quick Search</div>
  <div class="search"><svg width="12" height="12" viewBox="0 0 12 12"><circle cx="4.5" cy="4.5" r="3.5" fill="none" stroke="#999" stroke-width="1.5"/><line x1="7" y1="7" x2="11" y2="11" stroke="#999" stroke-width="2"/></svg></div>
  <div class="go">Go</div>
  <div class="tab" style="left:820px;top:140px;width:110px">Contact Us</div>
  <p class="footer-contact">info@tondashop.example<br>www.tondashop.example</p>
  <p class="copyright">© 2010 . Tondashop.example V3 . All Rights Reserved.</p>
</footer>
</body>
</html>
```